Plastic Business Card for Bookkeeper

We are looking for a simple professional business card design to use for printing on thin frosted plastic (see-through) card stock. Logo and brand guideline documents are attached as well as a photo of our old business card, and another business card example that we like.

Target Market(s)

Small Business

Industry/Entity Type

Bookkeeper

Contact Information for Business Card

Harriet Olsen CPA
Chief Executive Bookkeeper
T. 03 5926 4417
M. 0438 761 205
E. harriet@pinecrestledger.com
W. www.pinecrestledger.com

Font styles to use
Sans Serif

Colors
6b449b
00a990

Requirements
Must have
• Stick with logo colors. Writing should be clear and easy to read and not too cramped together.
Nice to have
• Tag line for back of the card - 'Not your ordinary Bookkeeper'

```html
<!DOCTYPE html>
<html lang="en">
<head>
<meta charset="utf-8">
<title>Pinecrest Ledger – Business Card</title>
<link href="https://fonts.googleapis.com/css2?family=Montserrat:wght@400;500;700&display=swap" rel="stylesheet">
<style>
  :root {
    --page-bg: #e4e8ea;
    --card-frost: #f3f6f7;
    --brand-purple: #734ea0;
    --brand-teal: #077a8a;
    --silver: #d9dde0;
    --ink-light: #ffffff;
  }
  * { margin: 0; padding: 0; box-sizing: border-box; }
  html, body {
    width: 1200px;
    height: 900px;
    overflow: hidden;
    background: var(--page-bg);
    font-family: "Montserrat", Arial, sans-serif;
  }
  .card {
    position: absolute;
    left: 120px;
    top: 167px;
    width: 960px;
    height: 566px;
    border-radius: 22px;
    overflow: hidden;
    background: var(--card-frost);
    box-shadow: 0 10px 30px rgba(0,0,0,0.12);
  }
  .card-shapes {
    position: absolute;
    inset: 0;
    width: 100%;
    height: 100%;
  }
  .brand {
    position: absolute;
    left: 40px;
    top: 200px;
    width: 360px;
    text-align: center;
  }
  .brand-dot {
    display: block;
    width: 92px;
    height: 92px;
    margin: 0 auto 26px;
    border-radius: 50%;
    background: var(--brand-teal);
  }
  .brand-name {
    color: var(--brand-purple);
    font-weight: 500;
    font-size: 34px;
    line-height: 1.3;
    letter-spacing: 0.5px;
    text-transform: uppercase;
  }
  .contact {
    position: absolute;
    right: 47px;
    color: var(--ink-light);
    text-align: right;
  }
  .person { top: 62px; }
  .person-name {
    font-size: 35px;
    font-weight: 700;
    line-height: 1.15;
  }
  .person-name .credential { font-weight: 500; }
  .person-title {
    font-size: 27px;
    font-weight: 500;
    margin-top: 6px;
  }
  .phones { top: 192px; }
  .phone-line {
    display: flex;
    align-items: center;
    justify-content: flex-end;
    gap: 10px;
    font-size: 29px;
    font-weight: 500;
    line-height: 44px;
  }
  .phone-line svg { width: 24px; height: 28px; }
  .online { top: 430px; }
  .online-line {
    font-size: 30px;
    font-weight: 500;
    line-height: 40px;
  }
</style>
</head>
<body>
  <div class="card">
    <svg class="card-shapes" viewBox="0 0 628 370" preserveAspectRatio="none" aria-hidden="true">
      <path d="M185,370 C230,260 330,215 628,232 L628,370 Z" fill="var(--brand-teal)"/>
      <path d="M193,370 C240,262 335,222 628,232" fill="none" stroke="var(--silver)" stroke-width="2.5"/>
      <path d="M198,0 C225,150 360,232 628,226" fill="none" stroke="var(--silver)" stroke-width="2.5"/>
      <path d="M208,0 C235,140 365,222 628,214 L628,0 Z" fill="var(--brand-purple)"/>
    </svg>

    <div class="brand">
      <span class="brand-dot"></span>
      <div class="brand-name">Pinecrest Ledger</div>
    </div>

    <div class="contact person">
      <div class="person-name">Harriet Olsen <span class="credential">CPA</span></div>
      <div class="person-title">Chief Executive Bookkeeper</div>
    </div>

    <div class="contact phones">
      <div class="phone-line">03 5926 4417
        <svg viewBox="0 0 24 28" aria-hidden="true"><path d="M6 3c1 0 2 2.5 2.6 4 .3 1-.8 1.8-1.4 2.6 1 2.6 3 5 5.4 6.4.8-.6 1.6-1.6 2.6-1.3 1.5.5 4 1.6 4 2.6 0 1.4-1.6 3.6-3.4 3.6C9 21 3 13 3 6.4 3 4.6 4.6 3 6 3z" fill="none" stroke="#fff" stroke-width="2"/></svg>
      </div>
      <div class="phone-line">0438 761 205
        <svg viewBox="0 0 24 28" aria-hidden="true"><rect x="5" y="2" width="14" height="24" rx="2" fill="none" stroke="#fff" stroke-width="2"/><line x1="5" y1="21" x2="19" y2="21" stroke="#fff" stroke-width="2"/></svg>
      </div>
    </div>

    <div class="contact online">
      <div class="online-line">harriet@pinecrestledger.com</div>
      <div class="online-line">www.pinecrestledger.com</div>
    </div>
  </div>
</body>
</html>
```